Bref créative
Business card and stationery for painting company
Brightcoat finishes
Professional
Marek Dolvan
Owner
318 S Harlow Ave suite 204
Villa Park, IL 60139
marek.dolvan@brightcoatfinishes.com
www.brightcoatfinishes.com
this is file of my logo
vector logo file

```html
<!DOCTYPE html>
<html lang="en">
<head>
<meta charset="utf-8">
<title>Brightcoat Finishes — Stationery Set</title>
<link rel="stylesheet" href="https://fonts.googleapis.com/css2?family=Montserrat:wght@400;600;700&display=swap">
<style>
  :root {
    --bg: #f1f1f1;
    --panel: #ffffff;
    --panel-line: #d9d9d9;
    --paper: #ffffff;
    --ink: #3a3a3a;
    --brand-blue: #2e4d99;
    --brand-red: #c9212b;
    --red-dark: #9e141c;
    --flap-line: #bdbdbd;
    --shadow: rgba(0,0,0,0.22);
  }
  * { box-sizing: border-box; margin: 0; padding: 0; }
  html, body { width: 1200px; height: 681px; overflow: hidden; background: var(--bg); }
  body { position: relative; font-family: "Montserrat", Arial, sans-serif; color: var(--ink); }

  .presentation-board {
    position: absolute; left: 19px; top: 43px; width: 1162px; height: 610px;
    background: var(--panel); border: 1px solid var(--panel-line);
  }
  .sheet {
    position: absolute; background: var(--paper);
    box-shadow: 2px 3px 6px var(--shadow);
  }

  /* brand wordmark */
  .wordmark { display: flex; align-items: center; gap: 6px; }
  .wordmark__dot { border-radius: 50%; background: var(--brand-red); flex: none; }
  .wordmark__name {
    font-weight: 700; color: var(--brand-blue); text-transform: uppercase;
    line-height: 1.05; letter-spacing: 0.5px;
  }

  /* brand band */
  .brand-band { position: absolute; left: 0; right: 0; display: flex; gap: 6px; }
  .brand-band__red { background: var(--brand-red); }
  .brand-band__blue { background: var(--brand-blue); }

  /* envelope front */
  .envelope-front { left: 60px; top: 96px; width: 497px; height: 216px; }
  .envelope-front .wordmark { position: absolute; left: 14px; top: 18px; }
  .envelope-front .wordmark__dot { width: 20px; height: 20px; }
  .envelope-front .wordmark__name { font-size: 17px; width: 110px; }
  .envelope-front .return-address { position: absolute; left: 14px; top: 80px; font-size: 6px; }
  .envelope-front .brand-band { top: 196px; height: 7px; }
  .envelope-front .brand-band__red { width: 236px; }
  .envelope-front .brand-band__blue { flex: 1; }

  /* envelope back */
  .envelope-back { left: 60px; top: 379px; width: 497px; height: 209px; }
  .envelope-back svg { position: absolute; left: 0; top: 0; }
  .envelope-back .wordmark { position: absolute; left: 50%; top: 92px; transform: translateX(-50%); }
  .envelope-back .wordmark__dot { width: 14px; height: 14px; }
  .envelope-back .wordmark__name { font-size: 10px; white-space: nowrap; }

  /* letterhead */
  .letterhead { left: 612px; top: 96px; width: 252px; height: 533px; }
  .letterhead .wordmark { position: absolute; left: 50%; top: 16px; transform: translateX(-50%); }
  .letterhead .wordmark__dot { width: 18px; height: 18px; }
  .letterhead .wordmark__name { font-size: 14px; width: 100px; }
  .letterhead .sender-block { position: absolute; left: 14px; top: 86px; font-size: 5.5px; line-height: 1.75; }
  .letterhead .brand-band { top: 515px; height: 4px; gap: 4px; }
  .letterhead .brand-band__red { width: 118px; }
  .letterhead .brand-band__blue { flex: 1; }

  /* business card front */
  .card-front { left: 972px; top: 312px; width: 156px; height: 96px; }
  .card-front .wordmark { position: absolute; left: 8px; top: 12px; gap: 3px; }
  .card-front .wordmark__dot { width: 9px; height: 9px; }
  .card-front .wordmark__name { font-size: 7px; width: 48px; }
  .card-front .holder { position: absolute; left: 84px; top: 12px; font-size: 5.5px; line-height: 1.5; }
  .card-front .holder__name { font-weight: 600; }
  .card-front .contact { position: absolute; left: 8px; top: 62px; font-size: 4px; line-height: 1.55; }

  /* business card back */
  .card-back {
    left: 972px; top: 432px; width: 156px; height: 108px;
    background: radial-gradient(circle at 50% 45%, var(--brand-red), var(--red-dark));
  }
  .card-back .wordmark { position: absolute; left: 50%; top: 50%; transform: translate(-50%, -50%); gap: 4px; }
  .card-back .wordmark__dot { width: 11px; height: 11px; background: #ffffff; }
  .card-back .wordmark__name { font-size: 8px; color: #ffffff; white-space: nowrap; }
</style>
</head>
<body>
  <div class="presentation-board"></div>

  <section class="sheet envelope-front" aria-label="Envelope front">
    <div class="wordmark"><span class="wordmark__dot"></span><span class="wordmark__name">Brightcoat Finishes</span></div>
    <p class="return-address">318 S Harlow Ave &nbsp;|&nbsp; Suite 204 &nbsp;|&nbsp; Oakridge Falls, WI 60139</p>
    <div class="brand-band"><span class="brand-band__red"></span><span class="brand-band__blue"></span></div>
  </section>

  <section class="sheet envelope-back" aria-label="Envelope back">
    <svg width="497" height="209" viewBox="0 0 497 209">
      <polyline points="0,0 248,78 497,0" fill="none" stroke="var(--flap-line)" stroke-width="1.2"/>
    </svg>
    <div class="wordmark"><span class="wordmark__dot"></span><span class="wordmark__name">Brightcoat Finishes</span></div>
  </section>

  <section class="sheet letterhead" aria-label="Letterhead">
    <div class="wordmark"><span class="wordmark__dot"></span><span class="wordmark__name">Brightcoat Finishes</span></div>
    <div class="sender-block">
      <p>318 S Harlow Ave</p>
      <p>Suite 204</p>
      <p>Oakridge Falls, WI 60139</p>
      <p>Phone: 630-555-0148</p>
      <p>marek.dolvan@brightcoatfinishes.com</p>
      <p>www.brightcoatfinishes.com</p>
    </div>
    <div class="brand-band"><span class="brand-band__red"></span><span class="brand-band__blue"></span></div>
  </section>

  <section class="sheet card-front" aria-label="Business card front">
    <div class="wordmark"><span class="wordmark__dot"></span><span class="wordmark__name">Brightcoat Finishes</span></div>
    <div class="holder">
      <p class="holder__name">Marek Dolvan</p>
      <p>Owner</p>
    </div>
    <div class="contact">
      <p>318 S Harlow Ave suite 204</p>
      <p>Oakridge Falls, WI 60139</p>
      <p>Phone: 630-555-0148</p>
      <p>marek.dolvan@brightcoatfinishes.com</p>
      <p>www.brightcoatfinishes.com</p>
    </div>
  </section>

  <section class="sheet card-back" aria-label="Business card back">
    <div class="wordmark"><span class="wordmark__dot"></span><span class="wordmark__name">Brightcoat Finishes</span></div>
  </section>
</body>
</html>
```